Business Card Design Project

We require a business card template to cover basic contact information - our company logo, names of employees, title, mobile and email.

Target Market(s)

Corporate

Industry/Entity Type

Business

Font styles to use
Sans Serif

Requirements
Nice to have
• Thinking it would be great just to have the logo taking up approximately half the space (so it goes as far across the top of the card as possible) and then contact details in the lower half of the card. Keen just to use only the two colours in the logo, on a white background.
Should not have
• No fussy drawings

```html
<!DOCTYPE html>
<html lang="en">
<head>
<meta charset="utf-8">
<title>Harbrook developments – Business Card</title>
<link rel="stylesheet" href="https://fonts.googleapis.com/css2?family=Questrial&display=swap">
<style>
  :root {
    --teal: #2aa9c0;
    --navy: #2b5c99;
    --ink: #1a1a1a;
    --paper: #ffffff;
    --edge: #9a9a9a;
  }
  * { margin: 0; padding: 0; box-sizing: border-box; }
  html, body {
    width: 1200px;
    height: 705px;
    overflow: hidden;
    background: var(--paper);
  }
  .card {
    position: relative;
    width: 1200px;
    height: 705px;
    background: var(--paper);
    border: 3px solid var(--edge);
    border-radius: 30px;
    font-family: "Questrial", "Century Gothic", sans-serif;
    overflow: hidden;
  }
  .brand {
    position: absolute;
    left: 0;
    right: 0;
    top: 40px;
    text-align: center;
    color: var(--teal);
  }
  .brand-name {
    display: block;
    font-size: 236px;
    line-height: 1;
    letter-spacing: -6px;
  }
  .brand-tagline {
    position: absolute;
    right: 150px;
    top: 262px;
    font-size: 62px;
    line-height: 1;
    letter-spacing: 1px;
  }
  .name-band {
    position: absolute;
    left: 143px;
    top: 483px;
    width: 912px;
    height: 57px;
  }
  .name-band svg { position: absolute; inset: 0; }
  .name-line {
    position: absolute;
    left: 82px;
    width: 745px;
    top: 0;
    height: 57px;
    display: flex;
    align-items: center;
    justify-content: center;
    gap: 14px;
    color: var(--paper);
  }
  .person { font-size: 41px; letter-spacing: 1px; }
  .role { font-size: 28px; }
  .contact {
    position: absolute;
    left: 0;
    right: 0;
    top: 562px;
    display: flex;
    justify-content: center;
    gap: 80px;
    font-size: 31px;
    font-style: italic;
    color: var(--ink);
  }
  .contact-label { color: var(--teal); margin-right: 10px; }
</style>
</head>
<body>
  <div class="card">
    <div class="brand">
      <span class="brand-name">Harbrook</span>
      <span class="brand-tagline">developments</span>
    </div>

    <div class="name-band">
      <svg width="912" height="57" viewBox="0 0 912 57" aria-hidden="true">
        <rect x="0" y="0" width="10" height="57" fill="var(--navy)"/>
        <rect x="17" y="0" width="8" height="57" fill="var(--navy)"/>
        <rect x="30" y="0" width="48" height="57" fill="var(--teal)"/>
        <rect x="82" y="0" width="745" height="57" fill="var(--navy)"/>
        <rect x="832" y="0" width="48" height="57" fill="var(--teal)"/>
        <rect x="887" y="0" width="8" height="57" fill="var(--navy)"/>
        <rect x="902" y="0" width="10" height="57" fill="var(--navy)"/>
      </svg>
      <div class="name-line">
        <span class="person">Daniel Hughes</span>
        <span class="role">| Director</span>
      </div>
    </div>

    <div class="contact">
      <span class="contact-item"><span class="contact-label">M:</span>0198 765 432</span>
      <span class="contact-item"><span class="contact-label">E:</span>daniel.hughes@mailbox.com</span>
    </div>
  </div>
</body>
</html>
```